Preferred pricing vendor

We are a plumbing company that has many services
-Boilers & Controls
-Plumbing & Heating
-HVAC & Refrigeration
-Preventative Maintenacne
-Gas fitting & Drain Cleaning

We primarily look after condo buildings, and our preferred service rates ($98, $93, or $88 depending on the contract) extend to all of our clients. So in essence, we look after the mechanical room and common equipment but our clients can call us in for drain cleaning or replacing a fixture in their suite. The discounted rates apply to the personal residence. We want a flyer to let them know they get a discount on our services. A one-pager we can send out to all of our contract clients.

Included source files for our letterhead and logo just so you can see the colours we go with.

Target Market(s)

Residential repairs, individual people, replacement of fixtures in-suite specific repairs

Requirements
Must have
• be colourful and attractive

```html
<!DOCTYPE html>
<html lang="en">
<head>
<meta charset="utf-8">
<title>Keystone Mechanical Inc – Discount Flyer</title>
<link href="https://fonts.googleapis.com/css2?family=Montserrat:wght@700;800;900&family=Roboto:wght@400;500;700&display=swap" rel="stylesheet">
<style>
  :root {
    --ink: #0d0f12;
    --blue: #2172c4;
    --blue-deep: #1d5fa8;
    --orange: #f2622e;
    --white: #ffffff;
    --navy-text: #1f2b44;
    --grey-band: #eeeff2;
    --body-grey: #4a4f58;
  }
  * { box-sizing: border-box; margin: 0; padding: 0; }
  html, body { width: 720px; height: 1200px; overflow: hidden; background: #e4e5e8; }
  .flyer {
    position: relative; width: 720px; height: 1200px; overflow: hidden;
    background: var(--white); font-family: "Roboto", Arial, sans-serif;
  }
  .backdrop { position: absolute; inset: 0; }
  .abs { position: absolute; }

  .brand { left: 48px; top: 82px; display: flex; align-items: center; gap: 14px; }
  .brand-dot { width: 62px; height: 62px; border-radius: 50%; background: var(--orange); }
  .brand-name {
    font-family: "Montserrat", Arial, sans-serif; font-weight: 900; font-size: 30px;
    color: var(--blue); letter-spacing: 0.5px; text-transform: uppercase; line-height: 1;
  }

  .headline { left: 48px; top: 204px; font-family: "Montserrat", Arial, sans-serif; font-weight: 900; line-height: 1.02; }
  .headline span { display: block; }
  .headline .h-blue { color: var(--blue); font-size: 46px; }
  .headline .h-white { color: var(--white); font-size: 35px; margin-top: 4px; }
  .headline .h-orange { color: var(--orange); font-size: 35px; margin-top: 2px; }

  .cities { left: 48px; top: 376px; font-family: "Montserrat", Arial, sans-serif; font-weight: 800; font-size: 23px; color: var(--blue); }
  .intro { left: 48px; top: 420px; width: 420px; color: var(--white); font-size: 16px; font-weight: 500; line-height: 1.2; }

  .discount-tag {
    left: 140px; top: 866px; font-family: "Montserrat", Arial, sans-serif; font-weight: 900;
    font-size: 20px; line-height: 1.15; color: var(--white); text-align: center;
  }
  .discount-tag span { display: block; background: var(--orange); padding: 1px 4px; margin-bottom: 3px; }

  .services-title {
    left: 358px; top: 694px; width: 268px; height: 52px; background: var(--orange);
    border-left: 12px solid var(--blue); color: var(--white);
    font-family: "Montserrat", Arial, sans-serif; font-weight: 900; font-size: 32px;
    display: flex; align-items: center; justify-content: center; letter-spacing: 0.5px;
  }
  .service-list { left: 404px; top: 766px; list-style: none; }
  .service-list li {
    display: flex; align-items: center; gap: 10px; height: 39px;
    font-size: 20px; font-weight: 700; color: var(--navy-text);
  }
  .service-list svg { width: 17px; height: 17px; flex: none; }

  .info-band { left: 0; top: 972px; width: 720px; height: 150px; background: var(--grey-band); }
  .rates-note { left: 42px; top: 996px; width: 140px; font-size: 12px; line-height: 1.35; color: var(--body-grey); }
  .price { top: 998px; width: 66px; height: 66px; border-radius: 50%; background: var(--blue);
    border: 5px solid var(--orange); box-shadow: 0 0 0 3px var(--white) inset;
    color: var(--white); font-weight: 700; font-size: 17px; display: flex; align-items: center; justify-content: center; }
  .contract-pill { left: 42px; top: 1080px; width: 334px; height: 24px; border-radius: 12px; background: var(--orange);
    color: var(--white); font-size: 12.5px; font-weight: 700; display: flex; align-items: center; justify-content: center; }
  .residence-note { left: 402px; top: 1004px; width: 278px; padding-left: 14px; border-left: 1.5px solid var(--blue);
    font-size: 12px; line-height: 1.42; color: var(--body-grey); text-align: justify; }

  .footer-contact { left: 0; top: 1121px; width: 452px; height: 79px; background: var(--blue); color: var(--white);
    display: flex; align-items: center; padding-left: 42px; gap: 28px; font-size: 15.5px; }
  .footer-address { left: 458px; top: 1121px; width: 262px; height: 79px; background: var(--orange); color: var(--white);
    display: flex; align-items: center; padding-left: 22px; gap: 8px; font-size: 15px; line-height: 1.25; }
  .contact-col { display: flex; flex-direction: column; gap: 4px; }
  .contact-col div { display: flex; align-items: center; gap: 7px; }
  .contact-col + .contact-col { border-left: 1px solid rgba(255,255,255,0.6); padding-left: 14px; }
  .icon-dot { width: 12px; height: 12px; border-radius: 50%; background: var(--orange); flex: none; display: flex; align-items: center; justify-content: center; }
  .icon-dot svg { width: 8px; height: 8px; }
</style>
</head>
<body>
<div class="flyer">
  <svg class="backdrop" width="720" height="1200" viewBox="0 0 720 1200">
    <defs>
      <linearGradient id="workerTone" x1="0" y1="0" x2="1" y2="1">
        <stop offset="0" stop-color="#1a1c20"/>
        <stop offset="0.55" stop-color="#3d4249"/>
        <stop offset="1" stop-color="#25292f"/>
      </linearGradient>
      <linearGradient id="plumberTone" x1="0" y1="0" x2="1" y2="1">
        <stop offset="0" stop-color="#f6b08f"/>
        <stop offset="0.5" stop-color="#3f6fc0"/>
        <stop offset="1" stop-color="#dfe6f2"/>
      </linearGradient>
    </defs>
    <rect x="0" y="0" width="720" height="600" fill="var(--ink)"/>
    <g role="img" aria-label="Photo of a technician in an orange hard hat and safety glasses servicing mechanical equipment">
      <path d="M300 0 H720 V520 C660 690 560 700 450 640 C380 600 330 560 300 540 Z" fill="url(#workerTone)"/>
    </g>
    <path d="M0 525 C150 520 300 620 440 690 C560 745 660 720 720 555 V1200 H0 Z" fill="var(--white)"/>
    <path d="M0 495 C150 470 300 560 450 640 C560 700 650 700 720 520 L720 555 C660 720 560 745 440 690 C300 620 150 520 0 525 Z" fill="var(--blue)"/>
    <g role="img" aria-label="Photo of a smiling plumber in blue overalls sitting cross-legged and pointing to the services, with a plunger beside him">
      <path d="M0 540 C120 560 260 630 395 700 V972 H0 Z" fill="url(#plumberTone)" opacity="0.9"/>
    </g>
  </svg>

  <div class="abs brand">
    <div class="brand-dot"></div>
    <div class="brand-name">Keystone Mechanical Inc</div>
  </div>

  <h1 class="abs headline">
    <span class="h-blue">AFFORDABLE</span>
    <span class="h-white">MECHANICAL SYSTEM</span>
    <span class="h-orange">MAINTENANCE</span>
  </h1>

  <p class="abs cities">CALGARY • EDMONTON</p>
  <p class="abs intro">We offer full-service solutions for commercial and condo buildings in Calgary and Edmonton</p>

  <p class="abs discount-tag"><span>DISCOUNT ON</span><span>OUR SERVICES</span></p>

  <h2 class="abs services-title">SERVICES</h2>
  <ul class="abs service-list">
    <li><svg viewBox="0 0 20 20"><circle cx="10" cy="10" r="8" fill="none" stroke="#f2622e" stroke-width="1.8"/><path d="M6 10.5l3 3 6-7" fill="none" stroke="#f2622e" stroke-width="1.8"/></svg>HVAC &amp; Refrigeration</li>
    <li><svg viewBox="0 0 20 20"><circle cx="10" cy="10" r="8" fill="none" stroke="#f2622e" stroke-width="1.8"/><path d="M6 10.5l3 3 6-7" fill="none" stroke="#f2622e" stroke-width="1.8"/></svg>Boilers &amp; Controls</li>
    <li><svg viewBox="0 0 20 20"><circle cx="10" cy="10" r="8" fill="none" stroke="#f2622e" stroke-width="1.8"/><path d="M6 10.5l3 3 6-7" fill="none" stroke="#f2622e" stroke-width="1.8"/></svg>Preventative Maintenacne</li>
    <li><svg viewBox="0 0 20 20"><circle cx="10" cy="10" r="8" fill="none" stroke="#f2622e" stroke-width="1.8"/><path d="M6 10.5l3 3 6-7" fill="none" stroke="#f2622e" stroke-width="1.8"/></svg>Plumbing &amp; Heating</li>
    <li><svg viewBox="0 0 20 20"><circle cx="10" cy="10" r="8" fill="none" stroke="#f2622e" stroke-width="1.8"/><path d="M6 10.5l3 3 6-7" fill="none" stroke="#f2622e" stroke-width="1.8"/></svg>Gas fitting &amp; Drain Cleaning</li>
  </ul>

  <div class="abs info-band"></div>
  <p class="abs rates-note">We primarily look after condo buildings, and our preferred service rates</p>
  <div class="abs price" style="left:184px">$98</div>
  <div class="abs price" style="left:248px">$93</div>
  <div class="abs price" style="left:314px">$88</div>
  <p class="abs contract-pill">Depending on the contract extend to all of our clients</p>
  <p class="abs residence-note">So in essence, we look after the mechanical room and common equipment but our clients can call us in for drain cleaning or replacing a fixture in their suite. The discounted rates apply to the personal residence.</p>

  <footer>
    <div class="abs footer-contact">
      <div class="contact-col">
        <div><span class="icon-dot"><svg viewBox="0 0 10 10"><path d="M2 1l2 2-1 1.2c.6 1.2 1.5 2.1 2.8 2.8L7 6l2 2-1.2 1.2C4.5 9 1 5.5.8 2.2Z" fill="#fff"/></svg></span>(403) 555-0142</div>
        <div><span class="icon-dot"><svg viewBox="0 0 10 10"><path d="M2 1l2 2-1 1.2c.6 1.2 1.5 2.1 2.8 2.8L7 6l2 2-1.2 1.2C4.5 9 1 5.5.8 2.2Z" fill="#fff"/></svg></span>(780) 555-0187</div>
      </div>
      <div class="contact-col">
        <div><span class="icon-dot"><svg viewBox="0 0 10 10"><circle cx="5" cy="5" r="3.5" fill="none" stroke="#fff" stroke-width="1.2"/></svg></span>www.keystonemech.ca</div>
        <div><span class="icon-dot"><svg viewBox="0 0 10 10"><rect x="1.5" y="2.5" width="7" height="5" fill="none" stroke="#fff" stroke-width="1.1"/><path d="M1.5 2.5l3.5 3 3.5-3" fill="none" stroke="#fff" stroke-width="1.1"/></svg></span>info@keystonemech.ca</div>
      </div>
    </div>
    <div class="abs footer-address">
      <svg width="14" height="18" viewBox="0 0 14 18" style="align-self:flex-start;margin-top:20px"><path d="M7 1C3.7 1 1.5 3.4 1.5 6.3 1.5 10 7 17 7 17s5.5-7 5.5-10.7C12.5 3.4 10.3 1 7 1Z" fill="#2172c4"/><circle cx="7" cy="6.4" r="2" fill="#fff"/></svg>
      <span>1-2210 48TH AVENUE SE,<br>CALGARY, ALBERTA</span>
    </div>
  </footer>
</div>
</body>
</html>
```